Dental Office Needs a Flyer Design to Attract New Patients

We need a flyer design for a dental office in Rockville, MD, US. Our office name is Brightpeak Dental Care. Our website is: brightpeakdentalcare.example and our office logo can be seen on the website. We would like stay that call and make an appointment with Dr. Le Ko. The flyer can follow the color scheme of our logo (blue and white). We current have Holiday/New Year special: Dental exam, x-ray, and cleaning for $95 (a $300 value); please include this in the flyer. Also if you can include a winter inspired picture to be part of the flyer, that would be great. We really like your Grin Tallowa flyer design and are looking for something similar. Thank you!
Target Market(s)
Apartment complex that is 5 minutes (less than 1 mile away)
Industry/Entity Type
Dental
Look and feel

```html
<!DOCTYPE html>
<html lang="en">
<head>
<meta charset="utf-8">
<title>Holiday/New Year Special – Brightpeak Dental Care</title>
<link rel="stylesheet" href="https://fonts.googleapis.com/css2?family=Fira+Sans:wght@600;700&display=swap">
<style>
  :root {
    --sky: #c9e5f7;
    --sky-light: #d9eefb;
    --frost: #ffffff;
    --brand-blue: #1069b4;
    --deep-blue: #1a5597;
    --offer-red: #e3141c;
    --logo-teal: #5fb3c9;
  }
  * { margin: 0; padding: 0; box-sizing: border-box; }
  html, body { width: 1200px; height: 509px; overflow: hidden; }
  body { font-family: "Fira Sans", Arial, sans-serif; }

  .flyer {
    position: relative;
    width: 1200px;
    height: 509px;
    overflow: hidden;
    background: linear-gradient(180deg, var(--sky-light) 0%, var(--sky) 100%);
  }

  .winter-art {
    position: absolute;
    left: 0;
    top: 0;
    width: 760px;
    height: 509px;
    background:
      radial-gradient(ellipse 360px 300px at 300px 390px, rgba(255,255,255,0.95) 0%, rgba(255,255,255,0.7) 45%, rgba(255,255,255,0) 100%),
      radial-gradient(ellipse 220px 180px at 70px 60px, rgba(255,255,255,0.9) 0%, rgba(255,255,255,0) 100%),
      linear-gradient(90deg, rgba(255,255,255,0.55) 0%, rgba(255,255,255,0.3) 55%, rgba(255,255,255,0) 100%);
  }

  .flurry {
    position: absolute;
    left: 520px;
    top: 0;
    width: 680px;
    height: 130px;
    background: linear-gradient(180deg, rgba(255,255,255,0.45) 0%, rgba(255,255,255,0) 100%);
  }

  .headline, .offer, .invite, .brand, .brand-url, .call-now {
    position: absolute;
    line-height: 1;
    white-space: nowrap;
  }

  .headline {
    right: 133px;
    top: 151px;
    font-size: 63px;
    font-weight: 600;
    color: var(--brand-blue);
  }

  .offer {
    right: 41px;
    top: 253px;
    font-size: 38px;
    font-weight: 600;
    color: var(--brand-blue);
  }
  .offer .price { color: var(--offer-red); }

  .invite {
    right: 62px;
    top: 314px;
    font-size: 30px;
    font-weight: 600;
    color: var(--brand-blue);
  }

  .brand {
    right: 96px;
    top: 383px;
    display: flex;
    align-items: center;
    gap: 10px;
  }
  .brand-mark {
    width: 30px;
    height: 30px;
    border-radius: 50%;
    background: var(--logo-teal);
  }
  .brand-name {
    font-size: 22px;
    font-weight: 600;
    color: var(--deep-blue);
  }
  .brand-url {
    right: 96px;
    top: 431px;
    font-size: 11px;
    font-weight: 600;
    color: var(--deep-blue);
  }

  .call-now {
    right: 26px;
    top: 466px;
    font-size: 32px;
    font-weight: 700;
    color: var(--deep-blue);
  }
</style>
</head>
<body>
  <main class="flyer">
    <div class="winter-art" role="img" aria-label="Large white paper-cut snowflakes filling the left side of a pale winter-blue sky"></div>
    <div class="flurry" role="img" aria-label="Small white snowflakes drifting across the top of the sky"></div>

    <h1 class="headline">Holiday/New Year Special</h1>
    <p class="offer">Dental Exam, X-ray, and Cleaning for <span class="price">$95</span> (a $300 value)</p>
    <p class="invite">Call and make an appointment with Dr. Le Ko</p>

    <div class="brand">
      <span class="brand-mark"></span>
      <span class="brand-name">Brightpeak Dental Care</span>
    </div>
    <p class="brand-url">brightpeakdentalcare.example</p>

    <p class="call-now">Call now 301-555-0147</p>
  </main>
</body>
</html>
```